Website re-design for a Gardening - Vegetable Growing -Compost Ecommerce site

We need a "green & organic" looking web design for The Loam Barrow website re-design. The website sells garden and landscape supplies, and specialises in composites and vegetable growing products which are sold nationwide throughout the UK.

This project is for a homepage & content page design which can be used as a template to create other pages through the site, ideally with css and coding for a joomla template.

Our customer base is made up of gardeners & vegetable growers. The site is an ecommerce site run on Joomla CMS, we will be converting the design into a joomla template.

The Home page will contain information and attractive garden & vegetable growing images linking to information and product / shop category pages.

Current site: www.theloambarrow.co.uk

Sites I like the look of :

http://fernquillplot.com/index.php
http://albumpage.stationnine.com
http://www.squirmydelvers.co.uk/
http://www.hamletcreamery.co.uk
Updates

Hi Guys! Feel free to use different colour schemes from the three colours i have suggested in the brief. I am open to any suggestions, but a modern look and feel is preferred.

Target Market(s)

Home owners, vegetable growers and keen gardeners

Industry/Entity Type

Landscape

Coding

Coded - Design and coding required

Font styles to use
Sans Serif

Colors
9bcb3c
faa54b
fece3e

Requirements
Must have
• a white main content background

```html
<!DOCTYPE html>
<html lang="en">
<head>
<meta charset="utf-8">
<title>The Loam Barrow – Home</title>
<link href="https://fonts.googleapis.com/css2?family=Roboto:wght@400;500;700&family=Roboto+Condensed:wght@400;700&display=swap" rel="stylesheet">
<style>
:root{
  --green:#4fa83d;
  --green-dark:#3f8f30;
  --green-text:#55a83a;
  --orange:#f5b81c;
  --ink:#222;
  --body:#666;
  --muted:#888;
  --line:#dcdcdc;
  --band:#e4e4e4;
  --footer:#333;
  --white:#fff;
}
*{box-sizing:border-box;margin:0;padding:0}
html,body{width:1200px;height:2412px;overflow:hidden;background:var(--white)}
body{font-family:"Roboto",Arial,sans-serif;color:var(--body);position:relative}
.abs{position:absolute}
a{color:inherit;text-decoration:none}

/* header */
.leaf-strip{left:0;top:0;width:1200px;height:34px;background:linear-gradient(180deg,#5c9a3a,#a6d179 70%,rgba(255,255,255,0))}
.brand{left:174px;top:50px;display:flex;align-items:center;gap:12px}
.brand-dot{width:40px;height:40px;border-radius:50%;background:var(--orange)}
.brand-name{font-size:30px;font-weight:700;color:var(--green);letter-spacing:-.5px}
.top-links{right:178px;top:42px;font-size:12px;color:#555;display:flex;gap:16px;align-items:center}
.phone-row{right:178px;top:72px;display:flex;align-items:center;gap:24px}
.phone{display:flex;align-items:center;gap:8px;font-size:19px;font-weight:500;color:#333}
.phone i{width:20px;height:20px;border-radius:50%;background:var(--green);display:inline-block}
.auth{font-size:12px;color:#555}
.nav{left:0;top:124px;width:1200px;height:52px;border-top:1px solid var(--line);border-bottom:1px solid var(--line)}
.nav ul{list-style:none;display:flex;position:absolute;left:174px;top:-1px;height:52px}
.nav li{height:52px;line-height:50px;padding:0 26px;font-size:14px;color:#333;border-left:1px solid var(--line)}
.nav li:last-child{border-right:1px solid var(--line)}
.nav li.active{border-top:3px solid var(--green);line-height:46px}

/* hero */
.hero{left:0;top:176px;width:1200px;height:382px;background:linear-gradient(180deg,#5c7d4a 0%,#4d6d38 45%,#6b6a4a 80%,#7a6b54 100%)}
.hero-caption{left:172px;top:306px;width:438px;height:132px;background:rgba(20,20,20,.72);padding:22px 24px}
.hero-caption h2{font-family:"Roboto Condensed",sans-serif;font-size:25px;font-weight:700;color:var(--white);margin-bottom:6px}
.hero-caption p{font-size:15px;line-height:20px;color:#eee}
.hero-dots{left:532px;top:416px;display:flex;gap:6px}
.hero-dots i{width:9px;height:9px;border-radius:50%;background:#ddd}
.hero-dots i:first-child{background:var(--orange)}
.hero-arrow{top:348px;width:38px;height:38px;border-radius:50%;background:rgba(255,255,255,.45)}

/* section titles */
.section-title{left:172px;width:850px;text-align:center;font-size:28px;font-weight:500;color:var(--ink)}
.section-title::before,.section-title::after{content:"";position:absolute;top:50%;width:215px;border-top:3px double #ccc}
.section-title::before{left:0}.section-title::after{right:0}
.welcome-text{left:188px;top:650px;width:820px;text-align:center;font-size:11.5px;line-height:18px;color:var(--muted)}
.welcome-text p+p{margin-top:10px}
.btn-more{left:552px;top:752px;width:92px;height:27px;background:var(--green);color:var(--white);font-size:12px;font-weight:500;text-align:center;line-height:27px;border-radius:2px}

/* categories */
.cat-box{left:172px;top:806px;width:192px;height:280px;background:#f2f2f2}
.cat-box h3{height:44px;background:var(--green);color:var(--white);font-size:19px;font-weight:500;text-align:center;line-height:44px}
.cat-box ul{list-style:none}
.cat-box li{height:34px;line-height:34px;padding-left:20px;font-size:13px;color:#666;border-bottom:1px solid var(--line);position:relative}
.cat-box li::before{content:"›";position:absolute;left:8px;color:#999}

.top-selling{left:412px;top:806px;width:610px;height:42px;background:var(--green)}
.top-selling h3{position:absolute;left:12px;top:0;height:42px;line-height:42px;font-size:19px;font-weight:700;color:var(--white)}
.top-selling .view-all{position:absolute;right:22px;top:13px;font-size:12px;color:#ffe066}
.products{left:428px;top:868px;display:flex;gap:20px}
.card{width:128px;height:216px;border:1px solid var(--line);text-align:center;font-size:11.5px}
.card h4{font-weight:400;font-size:11.5px;color:#333;height:36px;line-height:36px;white-space:nowrap}
.card .img{height:88px;margin:0 6px}
.card .was{margin-top:12px;color:#777;text-decoration:line-through}
.card .now{color:var(--green-text);font-size:15px;margin-top:4px}
.card .add{color:#2f86c9;margin-top:4px;font-size:11.5px;font-weight:500}
.chev{top:950px}

/* tabs */
.tabs{left:172px;top:1142px;display:flex}
.tabs span{height:24px;line-height:22px;padding:0 8px;font-size:11px;color:#333;border:1px solid var(--line);border-bottom:none;margin-right:-1px;background:#fff}
.tab-body{left:172px;top:1166px;width:440px;height:232px;border:1px solid var(--line)}
.thumbs{left:180px;top:1188px;width:132px}
.thumb{position:absolute;width:60px;height:58px}
.tab-copy{left:328px;top:1192px;width:270px;font-size:11.5px;line-height:16px;color:#777}
.tab-copy h4{font-size:14px;color:#222;font-weight:700;line-height:18px}
.tab-copy h5{font-size:13px;color:#222;font-weight:500;line-height:18px;margin-bottom:10px}
.tab-copy p+p{margin-top:12px}

.tech{left:654px;top:1144px;width:370px}
.tech h3{font-size:20px;font-weight:700;color:#222;margin-bottom:16px}
.tech .lead{color:var(--green-text);font-size:12.5px;line-height:16px;margin-bottom:12px}
.tech p{font-size:11.5px;line-height:16px;color:#777}
.tech ul{list-style:none;margin-top:14px}
.tech li{font-size:11.5px;line-height:26px;color:#777;padding-left:14px;position:relative}
.tech li::before{content:"›";position:absolute;left:0;color:#555}

/* why */
.video{left:172px;top:1526px;width:526px;height:256px;background:linear-gradient(160deg,#6e5240,#4a3428 60%,#5b4333)}
.video-shadow{left:190px;top:1782px;width:490px;height:14px;background:radial-gradient(ellipse at top,rgba(0,0,0,.25),rgba(0,0,0,0) 70%)}
.play{left:398px;top:1616px}
.timeline{left:764px;top:1500px;width:1px;height:330px;background:var(--line)}
.why-item{left:742px;width:290px}
.why-item i{position:absolute;left:0;top:0;width:46px;height:46px;border-radius:50%;background:var(--green);border:4px solid #fff;box-shadow:0 0 0 1px var(--line)}
.why-item svg{position:absolute;left:13px;top:13px}
.why-item h4{margin-left:64px;font-size:20px;font-weight:400;color:#222}
.why-item p{margin-left:64px;margin-top:6px;font-size:11.5px;line-height:15px;color:#888}

/* band */
.band{left:0;top:1892px;width:1200px;height:166px;background:var(--band)}
.band-col{top:1914px;width:220px;text-align:center}
.band-col .ico{width:56px;height:56px;border-radius:50%;border:2px solid #444;margin:0 auto 10px;display:flex;align-items:center;justify-content:center}
.band-col p{font-size:15px;color:#333}
.band-col strong{display:block;font-size:20px;font-weight:400;color:var(--green-text);margin-top:6px;letter-spacing:.5px}
.band-rule{top:1910px;width:1px;height:128px;background:#ccc}

/* footer */
.footer{left:0;top:2058px;width:1200px;height:280px;background:var(--footer)}
.footer-brand{left:172px;top:2196px;display:flex;align-items:center;gap:10px;color:#ddd;font-size:24px;font-weight:700}
.footer-brand span{width:32px;height:32px;border-radius:50%;background:#888}
.f-col{top:2116px;color:#ddd}
.f-col h4{font-size:16px;font-weight:700;color:var(--white);margin-bottom:18px}
.f-col ul{list-style:none}
.posts li{font-size:11.5px;line-height:14px;padding:8px 0;border-bottom:1px solid #444;width:150px}
.contact li{font-size:11.5px;line-height:15px;padding-left:22px;position:relative;margin-bottom:13px;width:200px}
.contact li::before{content:"";position:absolute;left:0;top:3px;width:9px;height:9px;border-radius:50%;background:#ccc}
.socials{display:flex;gap:16px;margin-top:6px}
.socials i{width:12px;height:12px;background:#ccc;display:block;border-radius:2px}
.photos{display:grid;grid-template-columns:repeat(3,60px);gap:6px}
.photos div{height:60px}
.bottom{left:0;top:2338px;width:1200px;height:74px;background:var(--green)}
.bottom p{position:absolute;left:174px;top:30px;font-size:11px;color:#fff}
.bottom .sq{position:absolute;top:20px;width:34px;height:34px;border-radius:2px}
</style>
</head>
<body>

<header>
  <div class="abs leaf-strip" role="img" aria-label="Hanging green leaves along the top edge"></div>
  <div class="abs brand"><span class="brand-dot"></span><span class="brand-name">The Loam Barrow</span></div>
  <div class="abs top-links">
    <span style="color:var(--green)">▾ 0 - item</span>
    <span>My Account&nbsp;|&nbsp;My Wishlist&nbsp;|&nbsp;Checkout</span>
  </div>
  <div class="abs phone-row">
    <div class="phone"><i></i>0800 555 01920</div>
    <div class="auth">Login &nbsp;|&nbsp; Register</div>
  </div>
  <nav class="abs nav">
    <ul>
      <li class="active">Home</li><li>Products</li><li>About Us</li><li>What We Do</li>
      <li>Garden Guru</li><li>Blog</li><li>Bulk Loads</li><li>Contact Us</li>
    </ul>
  </nav>
</header>

<section>
  <div class="abs hero" role="img" aria-label="Vegetable garden with rows of onions and a gardener tending the beds"></div>
  <div class="abs hero-arrow" style="left:38px"></div>
  <div class="abs hero-arrow" style="left:1122px"></div>
  <div class="abs hero-caption">
    <h2>100% PURE ORGANIC FERTILIZER</h2>
    <p>We supply a huge range of compost products including organic composts, peat free compost, etc all at unbeatable prices!</p>
  </div>
  <div class="abs hero-dots"><i></i><i></i><i></i></div>
</section>

<section>
  <h2 class="abs section-title" style="top:598px">Welcome to The Loam Barrow</h2>
  <div class="abs welcome-text">
    <p>We've got all the compost, topsoil and garden supplies you'll need to get your garden in shape this year! Whether you just need some compost to top up your flower beds or want to start growing your own fruit and veg, we have everything you'll need and much more!</p>
    <p>As the UK's leading supplier, we have an extensive range of growing media as well as many other garden products such as organic compost, vegetable growing kits and baby vegetable seedlings!</p>
  </div>
  <a class="abs btn-more">View more ●</a>
</section>

<section>
  <div class="abs cat-box">
    <h3>Categories</h3>
    <ul>
      <li>Compost &amp; Manure</li><li>Premium Topsoils</li><li>Grow Your Own</li>
      <li>Lawn Turf</li><li>Raised Bed Kits</li><li>Veg Plug Plants</li>
    </ul>
  </div>
  <div class="abs top-selling"><h3>Top Selling Products</h3><span class="view-all">View all ›</span></div>
  <svg class="abs chev" style="left:394px" width="20" height="40" viewBox="0 0 20 40"><path d="M17 2 3 20l14 18" fill="none" stroke="#222" stroke-width="2.5"/></svg>
  <svg class="abs chev" style="left:1002px" width="20" height="40" viewBox="0 0 20 40"><path d="M3 2l14 18L3 38" fill="none" stroke="#222" stroke-width="2.5"/></svg>
  <div class="abs products">
    <div class="card"><h4>Vegetable Topsoil</h4><div class="img" role="img" aria-label="Pile of dark topsoil" style="background:linear-gradient(#5a3f2c,#3a281c)"></div><div class="was">On Sale £118.80</div><div class="now">£84.00 inc.vat</div><div class="add">Add to cart ▾</div></div>
    <div class="card"><h4>Lawn Top Dressing</h4><div class="img" role="img" aria-label="Lawn being top dressed with a rake" style="background:linear-gradient(#b6a88a,#6f8a46)"></div><div class="was">On Sale £118.80</div><div class="now">£84.00 inc.vat</div><div class="add">Add to cart ▾</div></div>
    <div class="card"><h4>Ericaceous (acidic)</h4><div class="img" role="img" aria-label="Pink azalea flowers" style="background:linear-gradient(#e45a90,#b82f68)"></div><div class="was">On Sale £118.80</div><div class="now">£84.00 inc.vat</div><div class="add">Add to cart ▾</div></div>
    <div class="card"><h4>Raised Bed 1m x 1m</h4><div class="img" role="img" aria-label="Wooden raised bed with lettuce" style="background:linear-gradient(#8fc25a,#8a5c36)"></div><div class="was">On Sale £118.80</div><div class="now">£84.00 inc.vat</div><div class="add">Add to cart ▾</div></div>
  </div>
</section>

<section>
  <div class="abs tabs"><span>WHAT IS COMPOSET</span><span>SERVICES</span><span>AGRICULTURISTS</span></div>
  <div class="abs tab-body"></div>
  <div class="abs thumbs">
    <div class="thumb" role="img" aria-label="Bag of compost product" style="left:0;top:0;background:linear-gradient(#eee,#8aa36a)"></div>
    <div class="thumb" role="img" aria-label="Seedlings in soil" style="left:66px;top:0;background:linear-gradient(#4f7a3a,#3b2a1f)"></div>
    <div class="thumb" role="img" aria-label="Hand planting a seedling" style="left:0;top:66px;background:linear-gradient(#7fae5a,#5a4430)"></div>
  </div>
  <div class="abs tab-copy">
    <h4>Lorem ipsum dolor sit amet,</h4>
    <h5>Quisque non consectetur leo, sit amet accumsan nunc</h5>
    <p>Mauris euismod in augue vitae interdum. Phasellus sagittis maximus libero, laoreet blandit enim sodales in. Pellentesque vel ligula sed neque hendrerit commodo.</p>
    <p>Morbi at augue laoreet, ornare ante ac, sollicitudin nunc. Vivamus convallis porta lacus.</p>
  </div>
  <div class="abs tech">
    <h3>Implementing New Technologies</h3>
    <p class="lead">Mes cuml dia sed ineniasinge dolor commete ipsum comn etus curabitur faucibus.</p>
    <p>Phasellus sagittis maximus libero, laoreet blandit enim sodales in. Pellentesque vel ligula sed neque hendrerit commodo.</p>
    <ul>
      <li>Morbi at augue laoreet, ornare ante ac, sollicitudin nunc.</li>
      <li>Vivamus convallis porta lacus, vitae vulputate lorem</li>
      <li>Curabitur non magna pulvinar, porta lectus eget,</li>
      <li>Class aptent taciti sociosqu ad litora torquent per conubia</li>
    </ul>
  </div>
</section>

<section>
  <h2 class="abs section-title" style="top:1432px">Why You Choose Us</h2>
  <div class="abs video" role="img" aria-label="Close-up of rich dark compost, video still"></div>
  <div class="abs video-shadow"></div>
  <svg class="abs play" width="72" height="72" viewBox="0 0 72 72"><circle cx="36" cy="36" r="31" fill="none" stroke="#f5b81c" stroke-width="8"/><path d="M29 23v26l20-13z" fill="#f5b81c"/></svg>
  <div class="abs timeline"></div>
  <div class="abs why-item" style="top:1508px"><i></i><svg width="20" height="20" viewBox="0 0 20 20"><rect x="4" y="3" width="12" height="14" fill="none" stroke="#fff" stroke-width="2"/><path d="M7 8h6M7 12h6" stroke="#fff" stroke-width="2"/></svg><h4>Vestibulum eu biben</h4><p>Duis non quam varius, sagittis felis vitae, auctor enim. Nullam in metus quis ante pretium auctor.</p></div>
  <div class="abs why-item" style="top:1630px"><i></i><svg width="20" height="20" viewBox="0 0 20 20"><rect x="4" y="3" width="12" height="14" fill="none" stroke="#fff" stroke-width="2"/><path d="M7 8h6M7 12h6" stroke="#fff" stroke-width="2"/></svg><h4>Mauris et ipsum</h4><p>Duis non quam varius, sagittis felis vitae, auctor enim. Nullam in metus quis ante pretium auctor.</p></div>
  <div class="abs why-item" style="top:1750px"><i></i><svg width="20" height="20" viewBox="0 0 20 20"><rect x="4" y="3" width="12" height="14" fill="none" stroke="#fff" stroke-width="2"/><path d="M7 8h6M7 12h6" stroke="#fff" stroke-width="2"/></svg><h4>Fusce rutrum leo id</h4><p>Duis non quam varius, sagittis felis vitae, auctor enim. Nullam in metus quis ante pretium auctor.</p></div>
</section>

<section>
  <div class="abs band"></div>
  <div class="abs band-col" style="left:156px"><div class="ico"><svg width="26" height="26" viewBox="0 0 26 26"><rect x="6" y="3" width="14" height="20" rx="2" fill="#444"/></svg></div><p>Request a Compost</p><strong>CATALOGUE</strong></div>
  <div class="abs band-rule" style="left:374px"></div>
  <div class="abs band-col" style="left:376px"><div class="ico"><svg width="26" height="26" viewBox="0 0 26 26"><path d="M3 3h10l10 10-10 10L3 13z" fill="#444"/><circle cx="8" cy="8" r="2" fill="#e4e4e4"/></svg></div><p>All about Our</p><strong>DELIVERY</strong></div>
  <div class="abs band-rule" style="left:596px"></div>
  <div class="abs band-col" style="left:598px"><div class="ico"><svg width="26" height="26" viewBox="0 0 26 26"><rect x="4" y="10" width="18" height="13" fill="#444"/><rect x="3" y="7" width="20" height="4" fill="#444"/><path d="M13 7v16" stroke="#e4e4e4" stroke-width="2"/></svg></div><p>Compost Gift</p><strong>VOUCHERS</strong></div>
  <div class="abs band-rule" style="left:814px"></div>
  <div class="abs band-col" style="left:816px"><div class="ico"><svg width="26" height="26" viewBox="0 0 26 26"><rect x="3" y="11" width="5" height="12" fill="#444"/><path d="M10 11l5-8c2 0 3 1 3 3l-1 5h5c1 0 2 1 2 2l-2 9c0 1-1 1-2 1H10z" fill="#444"/></svg></div><p>Like Compost</p><strong>RECOMMENDED US</strong></div>
</section>

<footer>
  <div class="abs footer"></div>
  <div class="abs footer-brand"><span></span>The Loam Barrow</div>
  <div class="abs f-col posts" style="left:394px">
    <h4>Latest Post</h4>
    <ul><li>Curabitur ac neque at arcu</li><li>Proin vel mauris diam</li><li>Proin urna enim semper</li><li>Nunc adipiscing semper nisl</li><li>Pellentesque tempus semet</li></ul>
  </div>
  <div class="abs f-col contact" style="left:614px">
    <h4>Contact Info</h4>
    <ul>
      <li>Sales Office 12 Mill Lane, Hollowby Westshire WS4 9QT</li>
      <li>0871 555 0142</li>
      <li>info@theloambarrow.co.uk</li>
      <li>01632 960 418</li>
      <li>www.theloambarrow.co.uk</li>
    </ul>
    <div class="socials"><i></i><i></i><i></i><i></i></div>
  </div>
  <div class="abs f-col" style="left:834px">
    <h4>Photostream</h4>
    <div class="photos">
      <div role="img" aria-label="Garden bed photo" style="background:#7a5a3c"></div>
      <div role="img" aria-label="Green lawn photo" style="background:#6f9a45"></div>
      <div role="img" aria-label="Vegetable patch photo" style="background:#5d7a3d"></div>
      <div role="img" aria-label="Flowers photo" style="background:#8c4f4f"></div>
      <div role="img" aria-label="Turf roll photo" style="background:#3f5a2c"></div>
      <div role="img" aria-label="Pink flowers photo" style="background:#9b5a6e"></div>
    </div>
  </div>
  <div class="abs bottom">
    <p>Copyright © 2014 - All rights reserved.</p>
    <span class="sq" style="left:1034px;background:var(--orange)"></span>
    <span class="sq" style="left:1078px;background:#2f86e0"></span>
    <svg class="abs" style="left:1087px;top:30px" width="16" height="14" viewBox="0 0 16 14"><path d="M2 11l6-7 6 7" fill="none" stroke="#fff" stroke-width="2"/></svg>
    <svg class="abs" style="left:1042px;top:30px" width="18" height="14" viewBox="0 0 18 14"><rect x="1" y="1" width="16" height="12" fill="#fff"/><path d="M1 1l8 6 8-6" fill="none" stroke="#f5b81c" stroke-width="1.5"/></svg>
  </div>
</footer>

</body>
</html>
```